Flyer overhaul from current flyers

I need to have our current flyers updated with a fresher look. We also need to have a new utility and real estate flyer created that will go along with the design of the new flyer. We are looking for new pictures, new overall design, same color scheme but would like to have the flyers more airy and inviting.

Target Market(s)

decision makers in the healthcare/utilty/banking/real estate sectors

Font styles to use
Other font styles liked:
• Logo is in Bell MT

Colors
0054AA
0677BA
7BADD7
CADEEF
E8F1F8

Requirements
Must have
• Close to what is currently on the existing flyers

```html
<!DOCTYPE html>
<html lang="en">
<head>
<meta charset="utf-8">
<title>Tri-River Recovery – Healthcare Collections Flyer</title>
<link href="https://fonts.googleapis.com/css2?family=Roboto:wght@400;500;700;900&family=Roboto+Slab:wght@700&display=swap" rel="stylesheet">
<style>
  :root{
    --navy:#0054AA;
    --ocean:#0677BA;
    --deep:#0a4f7a;
    --sky:#7BADD7;
    --cyan:#19a8e0;
    --mist:#CADEEF;
    --frost:#E8F1F8;
    --ink:#111820;
    --white:#ffffff;
    --stage:#f2f3f5;
  }
  *{box-sizing:border-box;margin:0;padding:0}
  html,body{width:1200px;height:1200px;overflow:hidden}
  body{background:var(--stage);font-family:'Roboto',Arial,sans-serif;position:relative}

  .flyer{position:absolute;top:245px;width:546px;height:708px;background:var(--white);overflow:hidden}
  .flyer--front{left:35px}
  .flyer--back{left:622px}
  .flyer__shapes{position:absolute;inset:0;width:100%;height:100%}
  .abs{position:absolute}

  /* front */
  .brand{right:25px;top:40px;display:flex;align-items:center;gap:8px;color:var(--white);
         font-weight:700;font-size:15px;line-height:1.05;letter-spacing:.5px}
  .brand__dot{width:34px;height:34px;border-radius:50%;background:var(--white);flex:none}
  .title{left:30px;top:348px;font-size:28px;font-weight:700;color:var(--ink);letter-spacing:.2px}
  .tagline{left:0;top:412px;width:328px;height:32px;background:var(--cyan);color:var(--white);
           font-size:19px;font-weight:500;padding:5px 0 0 30px}
  .features{left:30px;top:460px;list-style:none}
  .features li{font-size:12.5px;font-weight:700;color:var(--ink);height:23px;padding-left:18px;position:relative}
  .features li::before{content:"";position:absolute;left:2px;top:3px;border-left:5px solid var(--ink);
                       border-top:4px solid transparent;border-bottom:4px solid transparent}
  .call-label{font-size:15px;font-weight:700;letter-spacing:.3px}
  .phone{font-size:24px;font-weight:700}
  .front-call{left:30px;top:598px;color:var(--ink)}
  .front-call .phone{margin-top:10px}
  .web{font-family:'Roboto Slab',Georgia,serif;font-size:12px;font-weight:700}
  .front-web{left:30px;top:684px;color:var(--deep)}
  .solution{left:334px;top:494px;color:var(--white);font-size:19px;font-weight:700;line-height:1.2}
  .services{left:350px;top:556px;color:var(--white);font-size:10.5px;line-height:13px;list-style:none}
  .services li{position:relative;padding-left:10px}
  .services li::before{content:"";position:absolute;left:0;top:5px;width:3px;height:3px;border-radius:50%;background:var(--white)}

  /* back */
  .heading{left:0;width:100%;top:322px;text-align:center;color:var(--white);font-size:42px;font-weight:700}
  .philosophy{left:38px;width:470px;top:395px;text-align:center;color:var(--white);font-size:11.6px;line-height:14.4px}
  .back-phone{left:31px;top:656px;color:var(--white)}
  .back-call{left:369px;top:640px;color:var(--white)}
  .back-web{left:325px;top:672px;color:var(--white)}
</style>
</head>
<body>

<section class="flyer flyer--front">
  <svg class="flyer__shapes" viewBox="0 0 546 708" aria-hidden="false">
    <defs>
      <linearGradient id="photoFront" x1="0" y1="0" x2="1" y2="1">
        <stop offset="0" stop-color="#1d2a38"/>
        <stop offset=".5" stop-color="#3f6f95"/>
        <stop offset="1" stop-color="#b9cbd9"/>
      </linearGradient>
      <linearGradient id="blueFront" x1="0" y1="0" x2="1" y2="0">
        <stop offset="0" stop-color="#2aa0d6"/>
        <stop offset="1" stop-color="#0a4f7a"/>
      </linearGradient>
    </defs>
    <path fill="url(#blueFront)" d="M546 290 V708 H300 L203 586 L430 400 C470 360 510 320 546 290 Z"/>
    <g role="img" aria-label="Photo of two healthcare workers reviewing records together">
      <path fill="url(#photoFront)" d="M0 0 H546 V300 C470 330 380 335 290 322 C170 300 70 230 0 130 Z"/>
    </g>
    <path fill="none" stroke="var(--cyan)" stroke-width="9" d="M0 135 C70 235 170 305 290 326 C380 340 470 334 546 304"/>
    <path fill="var(--ocean)" d="M0 0 H30 C10 30 2 70 0 110 Z"/>
  </svg>

  <div class="brand abs"><span class="brand__dot"></span><span>TRI-RIVER<br>RECOVERY</span></div>

  <h1 class="title abs">HEALTHCARE COLLECTIONS</h1>
  <p class="tagline abs">A Forward Thinking Approach</p>
  <ul class="features abs">
    <li>A Patient Friendly, Professional Approach</li>
    <li>Live, Online Agent Chat Portal</li>
    <li>Online Debt Negotiating Tools</li>
    <li>Online Dispute Resolution Tools</li>
    <li>501(r) Compliant</li>
  </ul>
  <div class="front-call abs"><p class="call-label">CALL US AT</p><p class="phone">(555) 214-7300</p></div>
  <p class="web front-web abs">www.tririverrecovery.com</p>

  <h2 class="solution abs">An Impactful,<br>All-In-One Solution</h2>
  <ul class="services abs">
    <li>Credit Report Monitoring</li>
    <li>Address/Phone Scrubbing</li>
    <li>Compliant Collection Letters</li>
    <li>Discretionary Credit Reporting</li>
    <li>Bankruptcy Claim Services</li>
    <li>Professional Skip Tracing</li>
    <li>Deceased/Probater Services</li>
    <li>Call Recording and Monitoring</li>
    <li>Legal Collection Services</li>
    <li>Customizable Collection Workflow</li>
  </ul>
</section>

<section class="flyer flyer--back">
  <svg class="flyer__shapes" viewBox="0 0 546 708">
    <defs>
      <linearGradient id="photoBack" x1="0" y1="0" x2="1" y2="1">
        <stop offset="0" stop-color="#cfc6bd"/>
        <stop offset=".6" stop-color="#9eb3c6"/>
        <stop offset="1" stop-color="#e6e2dc"/>
      </linearGradient>
      <radialGradient id="blueBack" cx=".5" cy=".2" r=".9">
        <stop offset="0" stop-color="#2bb0e6"/>
        <stop offset=".6" stop-color="#0d6c9f"/>
        <stop offset="1" stop-color="#0a4f7a"/>
      </radialGradient>
      <radialGradient id="blueLow" cx=".3" cy=".1" r=".9">
        <stop offset="0" stop-color="#1f9fd6"/>
        <stop offset="1" stop-color="#0a4f7a"/>
      </radialGradient>
    </defs>
    <g role="img" aria-label="Photo of a nurse walking with an elderly patient at home">
      <rect width="546" height="300" fill="url(#photoBack)"/>
    </g>
    <path fill="url(#blueBack)" d="M0 330 C120 250 420 250 546 330 V708 H0 Z"/>
    <path fill="url(#blueLow)" d="M0 570 C130 520 360 510 546 570 V708 H0 Z"/>
    <path fill="var(--ocean)" d="M0 0 H14 C6 20 2 40 0 60 Z"/>
  </svg>

  <h2 class="heading abs">Our Philosophy</h2>
  <p class="philosophy abs">Since our inception, and for over 40 years, healthcare collections have been at the center of our operation. Our philosophy is to provide consistent performance by investing in our clients accounts to ensure the maximum liquidation. By building on historically proven collection techniques and employing an ever-expanding access to data and technology, our agency has continued to improve our performance to the benefit of our clients. Our capital forward, compliance centered approach has proven to deliver consistent results to our healthcare providers.</p>
  <p class="phone back-phone abs">(555) 214-7300</p>
  <p class="call-label back-call abs">CALL US AT</p>
  <p class="web back-web abs">www.tririverrecovery.com</p>
</section>

</body>
</html>
```